Gather Every Thread Book Cover Design

We need:

Ebook and 6x 9 Inch trade paperback book cover (front, back, spine)

Book Title:Gather Every Thread
Subtitle: Getting Ready Before Hard Times Strike (Including Final Goodbyes) for Every Household

For a book written to help any of us gather the information needed to ensure we are set to take care of our loved ones in case of an emergency. Loved ones, a sense of urgency that leads to feeling calm and prepared is needed!

Target Market(s)

Any adult with children, a partner, parents or assets!

Industry/Entity Type

Financial Planning, Health care, Family

Font styles to use
Serif
Sans Serif

Colors
0054AA
0677BA
7BADD7
CADEEF
E8F1F8
FFF300
FFF600
FEFA6F
FFFEC7
FFFEE8
EE7325
F08F49
F5BC92
FAE3D3
FDF4ED
EB3D1F
EC4F4E
F09395
F8D3D4
FCEDEE

```html
<!DOCTYPE html>
<html lang="en">
<head>
<meta charset="UTF-8">
<title>Gather Every Thread — Book Cover</title>
<link rel="stylesheet" href="https://fonts.googleapis.com/css2?family=Kaushan+Script&family=Rubik+Distressed&family=Roboto+Condensed:wght@700&family=Montserrat:wght@500&display=swap">
<style>
  :root {
    --cover-blue: #1d2a8c;
    --cover-blue-deep: #141c6b;
    --cover-blue-light: #2f44b8;
    --title-red: #eb3d1f;
    --title-yellow: #fff300;
    --scene-red: #c8231c;
    --scene-dark: #3a0d12;
    --subtitle-white: #ffffff;
    --author-grey: #d9dbe8;
  }
  html, body {
    margin: 0;
    padding: 0;
    width: 800px;
    height: 1200px;
    overflow: hidden;
    background: var(--cover-blue-deep);
  }
  .cover {
    position: relative;
    width: 800px;
    height: 1200px;
    overflow: hidden;
    background: radial-gradient(ellipse 70% 55% at 50% 45%, var(--cover-blue-light) 0%, var(--cover-blue) 55%, var(--cover-blue-deep) 100%);
  }
  .cover-art {
    position: absolute;
    left: 60px;
    top: 360px;
    width: 690px;
    height: 450px;
    background:
      radial-gradient(ellipse 45% 55% at 42% 55%, var(--scene-red) 0%, rgba(200,35,28,0.75) 40%, rgba(58,13,18,0.55) 70%, rgba(29,42,140,0) 100%),
      linear-gradient(90deg, rgba(29,42,140,0) 0%, rgba(120,20,30,0.5) 30%, rgba(90,15,25,0.5) 70%, rgba(29,42,140,0) 100%);
    filter: blur(2px);
  }
  .title {
    position: absolute;
    left: 0;
    right: 0;
    top: 205px;
    margin: 0;
    text-align: center;
    font-weight: normal;
  }
  .title-script {
    display: block;
    font-family: "Kaushan Script", cursive;
    font-size: 84px;
    line-height: 1;
    color: var(--title-red);
    text-shadow: 2px 2px 0 #ffffff, -1px -1px 0 #ffffff;
  }
  .title-block {
    display: block;
    margin-top: 4px;
    font-family: "Rubik Distressed", sans-serif;
    font-size: 132px;
    line-height: 1;
    letter-spacing: 2px;
    color: var(--title-yellow);
  }
  .subtitle {
    position: absolute;
    left: 90px;
    right: 90px;
    top: 830px;
    margin: 0;
    text-align: center;
    font-family: "Roboto Condensed", sans-serif;
    font-weight: 700;
    font-size: 31px;
    line-height: 1.3;
    color: var(--subtitle-white);
  }
  .author {
    position: absolute;
    left: 0;
    right: 0;
    top: 1085px;
    margin: 0;
    text-align: center;
    font-family: "Montserrat", sans-serif;
    font-weight: 500;
    font-size: 30px;
    letter-spacing: 8px;
    color: var(--author-grey);
  }
</style>
</head>
<body>
  <main class="cover">
    <div class="cover-art" role="img" aria-label="Collage of emergency scenes: a hospital heart monitor, a crashed red car, and a dark tree with crows, blended in red tones"></div>
    <h1 class="title">
      <span class="title-script">Gather Every</span>
      <span class="title-block">THREAD</span>
    </h1>
    <p class="subtitle">Getting Ready Before Hard Times Strike (Including Final Goodbyes) for Every Household</p>
    <p class="author">MARISOL DENTON</p>
  </main>
</body>
</html>
```